UI Mockup For Online Scheduling Software

11.01.2018 - Brief Update:
The brief has not changed but the summary below as being added to aid designers.

- New file added "Updated 11.01.2018 - Individual Box" to clarify the sections. Specifically the primary tag section
- Improve on the current styling
- Consider changing the section layout to maximise the number of blocks displayed on screen (The sections dont not need to be stacked like the current version.
- The design is for the application running on a desktop PC with 16:9 screen aspect
- The design styling/layout should not look like the current version
- You may use the application to get an understanding of its workings at this link....https://marlowtesk.brivanlabs.com.au/
- Think outside the box....use your creative flare and show me something different to the current app (style and layout)

There are already some good submissions so closer to the deadline I will increase the budget and award $$$ to 1st and 2nd. The winner will be chosen to directly work on the remaining aspects of this application (setting page, mobile design, dashboard etc). The next design project associated to this application will be 10 time bigger than this one.

Good Luck Designers

*************************************************************
Redesign the user interface to make more efficient use of the screen real estate.

The software works by adding (Drag & Drop) Project Blocks to a Date Section. Then tags are added (Drag & Drop) to the block section below the header, and then resources are added to the block section below the tags.
Each block has 4 main sections that are stacked vertically:

1. Header - Displays Title and Address
2. Tags - Displays tags, maximum of 6 tags
3. Resources - Displays resources, maximum of 10 resources, NOTE: this section can be hidded.
4. Footer - Display basic stats (eg. 3 Resources assigned)

It is critical that as many block (20-30) as possible for a single date can be visible on screen.

The following criteria must be considered when mocking up layout:
1. Font Type, size, colour and emphasis
2. Block Colour/Shading, borders ect
3. Section Layout within the block (stacking & Alignment)
4. Mock ups to show scaled layout of blocks in both the open state and Closed State.
5. Mock up to display a minimum of 20 blocks.
6. Create a variation of your design that adds a 5th section. This will display the first tag only:
1. Header - Always Visible
2. Primary Tag - Always Visible
3. Secondary Tags - Can be hidden
4. Resources - Can be Hidden
5. Footer - Can be Hidden

Please be creative with your design and layout. I like a clean, minimalist design.
At this stage CSS file will not be required but would be benificial
Updates

Designs look the same

Target Market(s)

N/A

Industry/Entity Type

Software

Number of Pages Required

1 page

Font styles to use
Other font styles liked:
• Designers Choice

Colors

Designer to choose colors to be used in the design.

Requirements
Must have
• Variation to current layout and style
Should not have
• Same styling and layout as current design

```html
<!DOCTYPE html>
<html lang="en">
<head>
<meta charset="utf-8">
<title>Schedule Board</title>
<link href="https://fonts.googleapis.com/css2?family=Roboto:wght@400;500;700&display=swap" rel="stylesheet">
<style>
:root{
  --navy:#0d2d5e;--page:#eef1f5;--side:#f4f6f8;--side-item:#e3ebf3;--side-accent:#2a6fb5;
  --ink:#222;--muted:#555;--line:#c9ced4;--card-head:#e9eaec;--card:#fff;--resbox:#eeeeee;
  --trade:#cfe2f6;--trade-line:#9fc3ea;--ok:#8fd6a1;--ok-line:#6cc383;--x:#d9302f;
  --teal:#2cb3a1;--dark:#1b1b1b;--blue:#2a80c5;
}
*{box-sizing:border-box;margin:0;padding:0}
html,body{width:782px;height:1200px;overflow:hidden}
body{font-family:"Roboto",Arial,sans-serif;color:var(--ink);background:var(--page);position:relative}
.topbar{position:absolute;left:0;top:0;width:782px;height:39px;background:var(--navy);color:#fff}
.brand{position:absolute;left:13px;top:12px;font-size:12px;font-weight:700;letter-spacing:.2px}
.search{position:absolute;left:565px;top:10px;width:91px;height:18px;border:1px solid #6f86ab;border-radius:9px;font-size:7px;color:#cfd8e6;padding:4px 7px}
.search svg{position:absolute;right:6px;top:4px;width:8px;height:8px}
.welcome{position:absolute;left:676px;top:13px;font-size:9px;display:flex;align-items:center;gap:3px}
.topgear{position:absolute;left:728px;top:12px;width:12px;height:12px}
.caret{position:absolute;left:742px;top:17px;border:3px solid transparent;border-top-color:#fff}
.sidebar{position:absolute;left:0;top:39px;width:102px;height:1161px;background:var(--side);box-shadow:1px 0 3px rgba(0,0,0,.12)}
.nav{list-style:none;margin-top:4px}
.nav li{height:19px;margin-bottom:2px;background:var(--side-item);border-left:2px solid var(--side-accent);font-size:8.5px;display:flex;align-items:center;padding-left:16px;gap:6px;color:#333}
.nav svg{width:9px;height:8px}
.filterbar{position:absolute;left:102px;top:39px;width:680px;height:36px;background:#fff}
.filter-title{position:absolute;left:20px;top:13px;font-size:8.5px;display:flex;align-items:center;gap:4px}
.field{position:absolute;top:9px;height:18px;border:1px solid #cfd3d8;border-radius:2px;font-size:7px;color:#444;padding:5px 6px;background:#fff}
.field svg{position:absolute;right:5px;top:5px;width:7px;height:7px}
.field .dd{position:absolute;right:6px;top:7px;border:2.5px solid transparent;border-top-color:#444}
.btn{position:absolute;top:9px;height:18px;border-radius:2px;font-size:7px;color:#fff;text-align:center;line-height:18px}
.board{position:absolute;left:122px;top:92px;width:629px;height:974px;border:1px solid #a9b2bd;background:var(--page)}
.board-head{height:36px;background:#fff;margin:0;position:relative}
.day{position:absolute;left:10px;top:8px;font-size:8.5px}
.note{position:absolute;left:10px;top:20px;font-size:6px;color:#444}
.stats-line{position:absolute;right:16px;top:13px;font-size:6.5px;color:#333}
.grid{position:absolute;left:8px;top:49px;display:grid;grid-template-columns:repeat(5,118px);grid-auto-rows:216px;column-gap:5.5px;row-gap:14px}
.block{position:relative;background:var(--card);border:1px solid #d6d9dd;box-shadow:0 1px 2px rgba(0,0,0,.08)}
.block-head{height:27px;background:var(--card-head);padding:5px 24px 5px 9px}
.block-title{font-size:7.5px;font-weight:400;color:#222;white-space:nowrap;overflow:hidden;text-overflow:ellipsis}
.block-addr{font-size:5px;color:#555;margin-top:1px;white-space:nowrap}
.gear{position:absolute;right:11px;top:9px;width:9px;height:9px}
.tags,.res{list-style:none;position:absolute}
.tags{left:13px;top:38px;width:92px}
.res{left:9px;top:107px;width:101px;height:90px;background:var(--resbox);border:1px solid #cdd1d5;padding:10px 4px 0}
.pill{position:relative;height:12px;margin-bottom:4.2px;border:1px solid var(--line);background:#fff;font-size:6px;line-height:10px;padding-left:9px;border-radius:1px}
.pill .ic{position:absolute;left:3px;top:2.5px;width:5px;height:5px}
.pill b{position:absolute;right:4px;top:0;color:var(--x);font-size:8px;line-height:10px}
.trade{background:var(--trade);border-color:var(--trade-line)}
.ok{background:var(--ok);border-color:var(--ok-line)}
.stats{position:absolute;left:9px;top:206px;font-size:5px;color:#333}
.pager{position:absolute;left:122px;top:1075px;display:flex;gap:4.5px}
.pager span{height:13px;min-width:14px;padding:0 4px;border:1px solid #cfd3d8;background:#f7f7f7;font-size:6.5px;line-height:11px;text-align:center;color:#333}
.pager .on{background:var(--blue);color:#fff;border-color:var(--blue)}
.pager .wide{min-width:26px}
.footer{position:absolute;left:102px;top:1148px;width:680px;height:52px;background:#fff;text-align:center;font-size:6.5px;line-height:56px;color:#333}
</style>
</head>
<body>
<svg width="0" height="0" style="position:absolute">
  <defs>
    <symbol id="tagi" viewBox="0 0 10 10"><path d="M0 0h5l5 5-5 5-5-5z" fill="#333"/><circle cx="2.5" cy="2.5" r="1" fill="#fff"/></symbol>
    <symbol id="user" viewBox="0 0 10 10"><circle cx="5" cy="3" r="2.4" fill="#333"/><path d="M0.5 10c0-3 2-4.5 4.5-4.5S9.5 7 9.5 10z" fill="#333"/></symbol>
    <symbol id="gear" viewBox="0 0 20 20"><circle cx="10" cy="10" r="6.5" fill="none" stroke="currentColor" stroke-width="5" stroke-dasharray="3.4 1.7"/><circle cx="10" cy="10" r="5" fill="currentColor"/><circle cx="10" cy="10" r="2.2" fill="#e9eaec"/></symbol>
  </defs>
</svg>

<header class="topbar">
  <div class="brand">SPRAYFORM Works</div>
  <div class="search">Search<svg viewBox="0 0 10 10"><circle cx="4" cy="4" r="3" fill="none" stroke="#fff" stroke-width="1.4"/><path d="M6.2 6.2 9 9" stroke="#fff" stroke-width="1.5"/></svg></div>
  <div class="welcome"><svg width="9" height="8" viewBox="0 0 10 9"><path d="M5 0 0 4.5h1.5V9h2.5V6h2v3h2.5V4.5H10z" fill="#fff"/></svg>Welcome</div>
  <svg class="topgear" style="color:#fff"><use href="#gear"/></svg>
  <span class="caret"></span>
</header>

<aside class="sidebar">
  <ul class="nav">
    <li><svg viewBox="0 0 10 8"><path d="M0 8a5 5 0 0 1 10 0z" fill="#d9534f"/></svg>Dashboard</li>
    <li><svg viewBox="0 0 10 8"><rect x="0.5" y="0.5" width="9" height="5.5" fill="none" stroke="#d9534f"/><path d="M3 8h4" stroke="#d9534f"/></svg>Projects</li>
    <li><svg viewBox="0 0 10 8"><path d="M0 1h10M0 4h10M0 7h10" stroke="#d9534f" stroke-width="1.3"/></svg>Resources</li>
    <li><svg viewBox="0 0 10 8"><path d="M0 1h10M0 4h10M0 7h10" stroke="#d9534f" stroke-width="1.3"/></svg>Plants</li>
    <li><svg viewBox="0 0 10 8"><path d="M0 1h10M0 4h10M0 7h10" stroke="#d9534f" stroke-width="1.3"/></svg>Tags</li>
    <li><svg viewBox="0 0 10 8"><path d="M0 1h10M0 4h10M0 7h10" stroke="#d9534f" stroke-width="1.3"/></svg>Clients</li>
  </ul>
</aside>

<section class="filterbar">
  <div class="filter-title"><svg width="10" height="8" viewBox="0 0 10 8"><circle cx="3" cy="4" r="2.7" fill="#333"/><circle cx="7" cy="4" r="2.7" fill="#333"/></svg>Filter By Date</div>
  <div class="field" style="left:179px;width:65px">10-01-2018<svg viewBox="0 0 8 8"><rect x=".5" y="1" width="7" height="6.5" fill="none" stroke="#444"/><path d="M.5 3h7" stroke="#444"/></svg></div>
  <div class="field" style="left:252px;width:65px">24-01-2018<svg viewBox="0 0 8 8"><rect x=".5" y="1" width="7" height="6.5" fill="none" stroke="#444"/><path d="M.5 3h7" stroke="#444"/></svg></div>
  <div class="field" style="left:326px;width:64px">Select Project<span class="dd"></span></div>
  <div class="field" style="left:399px;width:65px">Select Client<span class="dd"></span></div>
  <div class="field" style="left:472px;width:65px">Select Tags<span class="dd"></span></div>
  <div class="btn" style="left:544px;width:48px;background:var(--teal)">Apply Filter</div>
  <div class="btn" style="left:600px;width:48px;background:var(--dark)">Clear Filter</div>
</section>

<main class="board">
  <div class="board-head">
    <div class="day">09-Jan-2018 [Tuesday]</div>
    <div class="note">Note: The first name in Bold is the supervisor</div>
    <div class="stats-line">Comment &nbsp;|&nbsp; Projects assigned 15 of 67 &nbsp;|&nbsp; Resoures scheduled 50 of 55</div>
  </div>
  <div class="grid">
    <!-- row 1 -->
    <div class="block"><div class="block-head"><div class="block-title">21356 - KRV Dale east</div><div class="block-addr">BRQ - Harlan St.Eastvale</div><svg class="gear"><use href="#gear"/></svg></div>
      <ul class="tags"><li class="pill trade"><svg class="ic"><use href="#tagi"/></svg>Trade: Shotcrete<b>×</b></li><li class="pill"><svg class="ic"><use href="#tagi"/></svg>Task: Piled Walls<b>×</b></li><li class="pill"><svg class="ic"><use href="#tagi"/></svg>Star: 6:43am<b>×</b></li><li class="pill ok"><svg class="ic"><use href="#tagi"/></svg>Confirmed<b>×</b></li></ul>
      <ul class="res"><li class="pill"><svg class="ic"><use href="#user"/></svg>Danny K<b>×</b></li><li class="pill"><svg class="ic"><use href="#user"/></svg>Marco P<b>×</b></li><li class="pill"><svg class="ic"><use href="#user"/></svg>Sam R<b>×</b></li></ul>
      <p class="stats">3 Resources, 0 Plant Assigned</p></div>
    <div class="block"><div class="block-head"><div class="block-title">21485 - Wattlefield</div><div class="block-addr">BRQ - Harlan St.Eastvale</div><svg class="gear"><use href="#gear"/></svg></div>
      <ul class="tags"><li class="pill trade"><svg class="ic"><use href="#tagi"/></svg>Trade: Shotcrete<b>×</b></li><li class="pill"><svg class="ic"><use href="#tagi"/></svg>Task: Piled Walls<b>×</b></li><li class="pill"><svg class="ic"><use href="#tagi"/></svg>Star: 6:43am<b>×</b></li><li class="pill ok"><svg class="ic"><use href="#tagi"/></svg>Confirmed<b>×</b></li></ul>
      <ul class="res"><li class="pill"><svg class="ic"><use href="#user"/></svg>Owen T<b>×</b></li><li class="pill"><svg class="ic"><use href="#user"/></svg>Marco P<b>×</b></li><li class="pill"><svg class="ic"><use href="#user"/></svg>Danny K<b>×</b></li><li class="pill"><svg class="ic"><use href="#user"/></svg>Marco P<b>×</b></li><li class="pill"><svg class="ic"><use href="#user"/></svg>Sam R<b>×</b></li></ul>
      <p class="stats">3 Resources, 0 Plant Assigned</p></div>
    <div class="block"><div class="block-head"><div class="block-title">21356 - KRV Dale east</div><div class="block-addr">BRQ - Harlan St.Eastvale</div><svg class="gear"><use href="#gear"/></svg></div>
      <ul class="tags"><li class="pill trade"><svg class="ic"><use href="#tagi"/></svg>Trade: Shotcrete<b>×</b></li></ul>
      <ul class="res"><li class="pill"><svg class="ic"><use href="#user"/></svg>Danny K<b>×</b></li></ul>
      <p class="stats">3 Resources, 0 Plant Assigned</p></div>
    <div class="block"><div class="block-head"><div class="block-title">21485 - Wattlefield</div><div class="block-addr">BRQ - Harlan St.Eastvale</div><svg class="gear"><use href="#gear"/></svg></div>
      <ul class="tags"><li class="pill trade"><svg class="ic"><use href="#tagi"/></svg>Trade: Shotcrete<b>×</b></li><li class="pill"><svg class="ic"><use href="#tagi"/></svg>Task: Piled Walls<b>×</b></li><li class="pill"><svg class="ic"><use href="#tagi"/></svg>Star: 6:43am<b>×</b></li><li class="pill ok"><svg class="ic"><use href="#tagi"/></svg>Confirmed<b>×</b></li></ul>
      <ul class="res"><li class="pill"><svg class="ic"><use href="#user"/></svg>Owen T<b>×</b></li><li class="pill"><svg class="ic"><use href="#user"/></svg>Marco P<b>×</b></li><li class="pill"><svg class="ic"><use href="#user"/></svg>Danny K<b>×</b></li><li class="pill"><svg class="ic"><use href="#user"/></svg>Marco P<b>×</b></li><li class="pill"><svg class="ic"><use href="#user"/></svg>Sam R<b>×</b></li></ul>
      <p class="stats">3 Resources, 0 Plant Assigned</p></div>
    <div class="block"><div class="block-head"><div class="block-title">21356 - KRV Dale east</div><div class="block-addr">BRQ - Harlan St.Eastvale</div><svg class="gear"><use href="#gear"/></svg></div>
      <ul class="tags"><li class="pill trade"><svg class="ic"><use href="#tagi"/></svg>Trade: Shotcrete<b>×</b></li><li class="pill"><svg class="ic"><use href="#tagi"/></svg>Task: Piled Walls<b>×</b></li><li class="pill"><svg class="ic"><use href="#tagi"/></svg>Star: 6:43am<b>×</b></li><li class="pill ok"><svg class="ic"><use href="#tagi"/></svg>Confirmed<b>×</b></li></ul>
      <ul class="res"><li class="pill"><svg class="ic"><use href="#user"/></svg>Danny K<b>×</b></li><li class="pill"><svg class="ic"><use href="#user"/></svg>Marco P<b>×</b></li><li class="pill"><svg class="ic"><use href="#user"/></svg>Sam R<b>×</b></li></ul>
      <p class="stats">3 Resources, 0 Plant Assigned</p></div>
    <!-- row 2 -->
    <div class="block"><div class="block-head"><div class="block-title">21485 - Wattlefield</div><div class="block-addr">BRQ - Harlan St.Eastvale</div><svg class="gear"><use href="#gear"/></svg></div>
      <ul class="tags"><li class="pill trade"><svg class="ic"><use href="#tagi"/></svg>Trade: Shotcrete<b>×</b></li><li class="pill"><svg class="ic"><use href="#tagi"/></svg>Task: Piled Walls<b>×</b></li><li class="pill"><svg class="ic"><use href="#tagi"/></svg>Star: 6:43am<b>×</b></li><li class="pill ok"><svg class="ic"><use href="#tagi"/></svg>Confirmed<b>×</b></li></ul>
      <ul class="res"><li class="pill"><svg class="ic"><use href="#user"/></svg>Owen T<b>×</b></li><li class="pill"><svg class="ic"><use href="#user"/></svg>Marco P<b>×</b></li><li class="pill"><svg class="ic"><use href="#user"/></svg>Danny K<b>×</b></li><li class="pill"><svg class="ic"><use href="#user"/></svg>Marco P<b>×</b></li><li class="pill"><svg class="ic"><use href="#user"/></svg>Sam R<b>×</b></li></ul>
      <p class="stats">3 Resources, 0 Plant Assigned</p></div>
    <div class="block"><div class="block-head"><div class="block-title">21356 - KRV Dale east</div><div class="block-addr">BRQ - Harlan St.Eastvale</div><svg class="gear"><use href="#gear"/></svg></div>
      <ul class="tags"><li class="pill trade"><svg class="ic"><use href="#tagi"/></svg>Trade: Shotcrete<b>×</b></li><li class="pill"><svg class="ic"><use href="#tagi"/></svg>Task: Piled Walls<b>×</b></li><li class="pill"><svg class="ic"><use href="#tagi"/></svg>Star: 6:43am<b>×</b></li><li class="pill ok"><svg class="ic"><use href="#tagi"/></svg>Confirmed<b>×</b></li></ul>
      <ul class="res"><li class="pill"><svg class="ic"><use href="#user"/></svg>Danny K<b>×</b></li><li class="pill"><svg class="ic"><use href="#user"/></svg>Marco P<b>×</b></li><li class="pill"><svg class="ic"><use href="#user"/></svg>Sam R<b>×</b></li></ul>
      <p class="stats">3 Resources, 0 Plant Assigned</p></div>
    <div class="block"><div class="block-head"><div class="block-title">21485 - Wattlefield</div><div class="block-addr">BRQ - Harlan St.Eastvale</div><svg class="gear"><use href="#gear"/></svg></div>
      <ul class="tags"><li class="pill trade"><svg class="ic"><use href="#tagi"/></svg>Trade: Shotcrete<b>×</b></li><li class="pill"><svg class="ic"><use href="#tagi"/></svg>Task: Piled Walls<b>×</b></li><li class="pill"><svg class="ic"><use href="#tagi"/></svg>Star: 6:43am<b>×</b></li><li class="pill ok"><svg class="ic"><use href="#tagi"/></svg>Confirmed<b>×</b></li></ul>
      <ul class="res"><li class="pill"><svg class="ic"><use href="#user"/></svg>Owen T<b>×</b></li><li class="pill"><svg class="ic"><use href="#user"/></svg>Marco P<b>×</b></li><li class="pill"><svg class="ic"><use href="#user"/></svg>Danny K<b>×</b></li><li class="pill"><svg class="ic"><use href="#user"/></svg>Marco P<b>×</b></li><li class="pill"><svg class="ic"><use href="#user"/></svg>Sam R<b>×</b></li></ul>
      <p class="stats">3 Resources, 0 Plant Assigned</p></div>
    <div class="block"><div class="block-head"><div class="block-title">21356 - KRV Dale east</div><div class="block-addr">BRQ - Harlan St.Eastvale</div><svg class="gear"><use href="#gear"/></svg></div>
      <ul class="res"><li class="pill"><svg class="ic"><use href="#user"/></svg>Danny K<b>×</b></li><li class="pill"><svg class="ic"><use href="#user"/></svg>Marco P<b>×</b></li><li class="pill"><svg class="ic"><use href="#user"/></svg>Sam R<b>×</b></li></ul>
      <p class="stats">3 Resources, 0 Plant Assigned</p></div>
    <div class="block"><div class="block-head"><div class="block-title">21485 - Wattlefield</div><div class="block-addr">BRQ - Harlan St.Eastvale</div><svg class="gear"><use href="#gear"/></svg></div>
      <ul class="tags"><li class="pill trade"><svg class="ic"><use href="#tagi"/></svg>Trade: Shotcrete<b>×</b></li><li class="pill"><svg class="ic"><use href="#tagi"/></svg>Task: Piled Walls<b>×</b></li><li class="pill"><svg class="ic"><use href="#tagi"/></svg>Star: 6:43am<b>×</b></li><li class="pill ok"><svg class="ic"><use href="#tagi"/></svg>Confirmed<b>×</b></li></ul>
      <ul class="res"><li class="pill"><svg class="ic"><use href="#user"/></svg>Owen T<b>×</b></li><li class="pill"><svg class="ic"><use href="#user"/></svg>Marco P<b>×</b></li><li class="pill"><svg class="ic"><use href="#user"/></svg>Danny K<b>×</b></li><li class="pill"><svg class="ic"><use href="#user"/></svg>Marco P<b>×</b></li><li class="pill"><svg class="ic"><use href="#user"/></svg>Sam R<b>×</b></li></ul>
      <p class="stats">3 Resources, 0 Plant Assigned</p></div>
    <!-- row 3 -->
    <div class="block"><div class="block-head"><div class="block-title">21356 - KRV Dale east</div><div class="block-addr">BRQ - Harlan St.Eastvale</div><svg class="gear"><use href="#gear"/></svg></div>
      <ul class="tags"><li class="pill trade"><svg class="ic"><use href="#tagi"/></svg>Trade: Shotcrete<b>×</b></li><li class="pill"><svg class="ic"><use href="#tagi"/></svg>Task: Piled Walls<b>×</b></li><li class="pill"><svg class="ic"><use href="#tagi"/></svg>Star: 6:43am<b>×</b></li><li class="pill ok"><svg class="ic"><use href="#tagi"/></svg>Confirmed<b>×</b></li></ul>
      <ul class="res"><li class="pill"><svg class="ic"><use href="#user"/></svg>Danny K<b>×</b></li><li class="pill"><svg class="ic"><use href="#user"/></svg>Marco P<b>×</b></li><li class="pill"><svg class="ic"><use href="#user"/></svg>Sam R<b>×</b></li></ul>
      <p class="stats">3 Resources, 0 Plant Assigned</p></div>
    <div class="block"><div class="block-head"><div class="block-title">21485 - Wattlefield</div><div class="block-addr">BRQ - Harlan St.Eastvale</div><svg class="gear"><use href="#gear"/></svg></div>
      <ul class="tags"><li class="pill trade"><svg class="ic"><use href="#tagi"/></svg>Trade: Shotcrete<b>×</b></li></ul>
      <ul class="res"><li class="pill"><svg class="ic"><use href="#user"/></svg>Owen T<b>×</b></li></ul>
      <p class="stats">3 Resources, 0 Plant Assigned</p></div>
    <div class="block"><div class="block-head"><div class="block-title">21356 - KRV Dale east</div><div class="block-addr">BRQ - Harlan St.Eastvale</div><svg class="gear"><use href="#gear"/></svg></div>
      <ul class="tags"><li class="pill trade"><svg class="ic"><use href="#tagi"/></svg>Trade: Shotcrete<b>×</b></li><li class="pill"><svg class="ic"><use href="#tagi"/></svg>Task: Piled Walls<b>×</b></li><li class="pill"><svg class="ic"><use href="#tagi"/></svg>Star: 6:43am<b>×</b></li><li class="pill ok"><svg class="ic"><use href="#tagi"/></svg>Confirmed<b>×</b></li></ul>
      <ul class="res"><li class="pill"><svg class="ic"><use href="#user"/></svg>Danny K<b>×</b></li><li class="pill"><svg class="ic"><use href="#user"/></svg>Marco P<b>×</b></li><li class="pill"><svg class="ic"><use href="#user"/></svg>Sam R<b>×</b></li></ul>
      <p class="stats">3 Resources, 0 Plant Assigned</p></div>
    <div class="block"><div class="block-head"><div class="block-title">21485 - Wattlefield</div><div class="block-addr">BRQ - Harlan St.Eastvale</div><svg class="gear"><use href="#gear"/></svg></div>
      <ul class="tags"><li class="pill trade"><svg class="ic"><use href="#tagi"/></svg>Trade: Shotcrete<b>×</b></li><li class="pill"><svg class="ic"><use href="#tagi"/></svg>Task: Piled Walls<b>×</b></li><li class="pill"><svg class="ic"><use href="#tagi"/></svg>Star: 6:43am<b>×</b></li><li class="pill ok"><svg class="ic"><use href="#tagi"/></svg>Confirmed<b>×</b></li></ul>
      <ul class="res"><li class="pill"><svg class="ic"><use href="#user"/></svg>Owen T<b>×</b></li><li class="pill"><svg class="ic"><use href="#user"/></svg>Marco P<b>×</b></li><li class="pill"><svg class="ic"><use href="#user"/></svg>Danny K<b>×</b></li><li class="pill"><svg class="ic"><use href="#user"/></svg>Marco P<b>×</b></li><li class="pill"><svg class="ic"><use href="#user"/></svg>Sam R<b>×</b></li></ul>
      <p class="stats">3 Resources, 0 Plant Assigned</p></div>
    <div class="block"><div class="block-head"><div class="block-title">21356 - KRV Dale east</div><div class="block-addr">BRQ - Harlan St.Eastvale</div><svg class="gear"><use href="#gear"/></svg></div>
      <ul class="tags"><li class="pill trade"><svg class="ic"><use href="#tagi"/></svg>Trade: Shotcrete<b>×</b></li><li class="pill"><svg class="ic"><use href="#tagi"/></svg>Task: Piled Walls<b>×</b></li><li class="pill"><svg class="ic"><use href="#tagi"/></svg>Star: 6:43am<b>×</b></li><li class="pill ok"><svg class="ic"><use href="#tagi"/></svg>Confirmed<b>×</b></li></ul>
      <ul class="res"><li class="pill"><svg class="ic"><use href="#user"/></svg>Danny K<b>×</b></li><li class="pill"><svg class="ic"><use href="#user"/></svg>Marco P<b>×</b></li><li class="pill"><svg class="ic"><use href="#user"/></svg>Sam R<b>×</b></li></ul>
      <p class="stats">3 Resources, 0 Plant Assigned</p></div>
    <!-- row 4 -->
    <div class="block"><div class="block-head"><div class="block-title">21485 - Wattlefield</div><div class="block-addr">BRQ - Harlan St.Eastvale</div><svg class="gear"><use href="#gear"/></svg></div>
      <ul class="res" style="background:#fff;border-color:#fff"><li class="pill"><svg class="ic"><use href="#user"/></svg>Owen T<b>×</b></li><li class="pill"><svg class="ic"><use href="#user"/></svg>Marco P<b>×</b></li><li class="pill"><svg class="ic"><use href="#user"/></svg>Danny K<b>×</b></li><li class="pill"><svg class="ic"><use href="#user"/></svg>Marco P<b>×</b></li><li class="pill"><svg class="ic"><use href="#user"/></svg>Sam R<b>×</b></li></ul>
      <p class="stats">3 Resources, 0 Plant Assigned</p></div>
    <div class="block"><div class="block-head"><div class="block-title">21356 - KRV Dale east</div><div class="block-addr">BRQ - Harlan St.Eastvale</div><svg class="gear"><use href="#gear"/></svg></div>
      <ul class="tags"><li class="pill trade"><svg class="ic"><use href="#tagi"/></svg>Trade: Shotcrete<b>×</b></li><li class="pill"><svg class="ic"><use href="#tagi"/></svg>Task: Piled Walls<b>×</b></li><li class="pill"><svg class="ic"><use href="#tagi"/></svg>Star: 6:43am<b>×</b></li><li class="pill ok"><svg class="ic"><use href="#tagi"/></svg>Confirmed<b>×</b></li></ul>
      <ul class="res"><li class="pill"><svg class="ic"><use href="#user"/></svg>Danny K<b>×</b></li><li class="pill"><svg class="ic"><use href="#user"/></svg>Marco P<b>×</b></li><li class="pill"><svg class="ic"><use href="#user"/></svg>Sam R<b>×</b></li></ul>
      <p class="stats">3 Resources, 0 Plant Assigned</p></div>
    <div class="block"><div class="block-head"><div class="block-title">21485 - Wattlefield</div><div class="block-addr">BRQ - Harlan St.Eastvale</div><svg class="gear"><use href="#gear"/></svg></div>
      <ul class="tags"><li class="pill trade"><svg class="ic"><use href="#tagi"/></svg>Trade: Shotcrete<b>×</b></li><li class="pill"><svg class="ic"><use href="#tagi"/></svg>Task: Piled Walls<b>×</b></li><li class="pill"><svg class="ic"><use href="#tagi"/></svg>Star: 6:43am<b>×</b></li><li class="pill ok"><svg class="ic"><use href="#tagi"/></svg>Confirmed<b>×</b></li></ul>
      <ul class="res"><li class="pill"><svg class="ic"><use href="#user"/></svg>Owen T<b>×</b></li><li class="pill"><svg class="ic"><use href="#user"/></svg>Marco P<b>×</b></li><li class="pill"><svg class="ic"><use href="#user"/></svg>Danny K<b>×</b></li><li class="pill"><svg class="ic"><use href="#user"/></svg>Marco P<b>×</b></li><li class="pill"><svg class="ic"><use href="#user"/></svg>Sam R<b>×</b></li></ul>
      <p class="stats">3 Resources, 0 Plant Assigned</p></div>
    <div class="block"><div class="block-head"><div class="block-title">21356 - KRV Dale east</div><div class="block-addr">BRQ - Harlan St.Eastvale</div><svg class="gear"><use href="#gear"/></svg></div>
      <ul class="tags"><li class="pill trade"><svg class="ic"><use href="#tagi"/></svg>Trade: Shotcrete<b>×</b></li><li class="pill"><svg class="ic"><use href="#tagi"/></svg>Task: Piled Walls<b>×</b></li><li class="pill"><svg class="ic"><use href="#tagi"/></svg>Star: 6:43am<b>×</b></li><li class="pill ok"><svg class="ic"><use href="#tagi"/></svg>Confirmed<b>×</b></li></ul>
      <ul class="res"><li class="pill"><svg class="ic"><use href="#user"/></svg>Danny K<b>×</b></li><li class="pill"><svg class="ic"><use href="#user"/></svg>Marco P<b>×</b></li><li class="pill"><svg class="ic"><use href="#user"/></svg>Sam R<b>×</b></li></ul>
      <p class="stats">3 Resources, 0 Plant Assigned</p></div>
    <div class="block"><div class="block-head"><div class="block-title">21485 - Wattlefield</div><div class="block-addr">BRQ - Harlan St.Eastvale</div><svg class="gear"><use href="#gear"/></svg></div>
      <ul class="tags"><li class="pill trade"><svg class="ic"><use href="#tagi"/></svg>Trade: Shotcrete<b>×</b></li><li class="pill"><svg class="ic"><use href="#tagi"/></svg>Task: Piled Walls<b>×</b></li><li class="pill"><svg class="ic"><use href="#tagi"/></svg>Star: 6:43am<b>×</b></li><li class="pill ok"><svg class="ic"><use href="#tagi"/></svg>Confirmed<b>×</b></li></ul>
      <ul class="res" style="background:#fff;border-color:#fff"><li class="pill"><svg class="ic"><use href="#user"/></svg>Owen T<b>×</b></li><li class="pill"><svg class="ic"><use href="#user"/></svg>Marco P<b>×</b></li><li class="pill"><svg class="ic"><use href="#user"/></svg>Danny K<b>×</b></li><li class="pill"><svg class="ic"><use href="#user"/></svg>Marco P<b>×</b></li><li class="pill"><svg class="ic"><use href="#user"/></svg>Sam R<b>×</b></li></ul>
      <p class="stats">3 Resources, 0 Plant Assigned</p></div>
  </div>
</main>

<nav class="pager">
  <span class="wide">Prev</span><span class="on">1</span><span>2</span><span>3</span><span>4</span><span>5</span><span>6</span><span>...</span><span>22</span><span class="wide">Next</span>
</nav>

<footer class="footer">Copyright © 2018. All Rights Reserved</footer>
</body>
</html>
```